Executive Presence Book Cover for Larkmoor Coaching

I am looking for 10 book covers that are unified and work very well together. they have to be simple with an international feel.I will be using the colors of the rainbows for the color of the books and all I am looking for is a creative way to write the title of the book on the cover. The ten titles are as follows: Transparency, Humility, Poise ,Charisma ,Relationships, Results, Clarity, Being Present, Grooming and Appearance,Acumen

Target Market(s)

business executives

Font styles to use
Other font styles liked:
• use any font you think would work

Colors

Designer to choose colors to be used in the design.

Requirements
Must have
• simple, easy to read, looking for the word to be the focus/focal point of the cover. we will be putting information on the back cover of our company etc.
• only the words of the title nothing else. The size of the book is 9“ x 7“. The only thing on the outside of the book is the title, no author nothing else. We will be putting information on the back cover of the book in very simple font.
Nice to have
• i would like each title of the 10 book covers to be clean, consistent and elegant and corporate. as long as it is not too "SILLY" i would like the titles to speak of their purpose. for instance,
• charisma could have a letter that look elegant
• being present could have some bold letters.
Should not have
• alot of drawings or pictures
• they can't be jovial, light or humorous treatments.

```html
<!DOCTYPE html>
<html lang="en">
<head>
<meta charset="utf-8">
<title>Larkmoor Coaching – Executive Presence Series</title>
<link rel="stylesheet" href="https://fonts.googleapis.com/css2?family=Bebas+Neue&display=swap">
<style>
  :root {
    --page: #ffffff;
    --shadow: #b3b3b3;
    --ink: #ffffff;
    --transparency: #ed1c24;
    --humility: #f37046;
    --poise: #f0e213;
    --charisma: #8cc63f;
    --relationships: #26a9e0;
    --results: #283a8f;
    --clarity: #662d91;
    --being-present: #d91b5c;
    --grooming: #9b8579;
    --acumen: #8b5e3c;
    --cover-w: 234px;
    --cover-h: 302px;
  }
  * { margin: 0; padding: 0; box-sizing: border-box; }
  html, body { width: 1200px; height: 1200px; overflow: hidden; background: var(--page); }
  .series { position: relative; width: 1200px; height: 1200px; }

  .book { position: absolute; width: var(--cover-w); height: var(--cover-h); }
  .book-shadow {
    position: absolute; left: 8px; top: 14px;
    width: calc(var(--cover-w) + 6px); height: calc(var(--cover-h) + 2px);
    background: var(--shadow);
    clip-path: polygon(0 0, calc(100% - 12px) 0, 100% 12px, 100% 100%, 12px 100%, 0 calc(100% - 12px));
  }
  .book-gap {
    position: absolute; left: 0; top: 0;
    width: calc(var(--cover-w) + 5px); height: calc(var(--cover-h) + 5px);
    background: var(--page);
  }
  .cover {
    position: absolute; inset: 0; overflow: hidden;
    font-family: "Bebas Neue", "Oswald", sans-serif;
    font-weight: 400;
    color: var(--ink); text-align: center;
  }
  .cover-texture {
    position: absolute; left: 0; right: 0; top: 20px; bottom: 30px;
    background: linear-gradient(to bottom,
      rgba(255,255,255,0) 0%,
      rgba(255,255,255,0.10) 45%,
      rgba(255,255,255,0.10) 55%,
      rgba(255,255,255,0) 100%);
  }
  .cover--poise .cover-texture {
    background: linear-gradient(to bottom,
      rgba(255,255,255,0) 0%,
      rgba(255,255,255,0.18) 45%,
      rgba(255,255,255,0.18) 55%,
      rgba(255,255,255,0) 100%);
  }

  .title {
    position: absolute; left: 0; right: 0; top: 128px;
    font-size: 40px; line-height: 40px; font-weight: 400;
    white-space: nowrap; letter-spacing: 0.3px;
  }
  .title-phrase {
    position: absolute; left: 0; right: 0; top: 104px;
    font-weight: 400;
  }
  .title-phrase .big { display: block; font-size: 39px; line-height: 34px; height: 34px; }
  .title-phrase .small { display: block; font-size: 19px; line-height: 20px; height: 20px; }

  .cover--transparency { background: var(--transparency); }
  .cover--humility { background: var(--humility); }
  .cover--poise { background: var(--poise); }
  .cover--charisma { background: var(--charisma); }
  .cover--relationships { background: var(--relationships); }
  .cover--results { background: var(--results); }
  .cover--clarity { background: var(--clarity); }
  .cover--being-present { background: var(--being-present); }
  .cover--grooming { background: var(--grooming); }
  .cover--acumen { background: var(--acumen); }
</style>
</head>
<body>
<main class="series">

  <div class="book" style="left:62px; top:80px;">
    <div class="book-shadow"></div><div class="book-gap"></div>
    <section class="cover cover--transparency">
      <div class="cover-texture" role="img" aria-label="Faint tonal title pattern behind the word"></div>
      <h2 class="title">Transparency</h2>
    </section>
  </div>

  <div class="book" style="left:342px; top:80px;">
    <div class="book-shadow"></div><div class="book-gap"></div>
    <section class="cover cover--humility">
      <div class="cover-texture" role="img" aria-label="Faint tonal title pattern behind the word"></div>
      <h2 class="title">Humility</h2>
    </section>
  </div>

  <div class="book" style="left:623px; top:80px;">
    <div class="book-shadow"></div><div class="book-gap"></div>
    <section class="cover cover--poise">
      <div class="cover-texture" role="img" aria-label="Faint tonal title pattern behind the word"></div>
      <h2 class="title">Poise</h2>
    </section>
  </div>

  <div class="book" style="left:904px; top:80px;">
    <div class="book-shadow"></div><div class="book-gap"></div>
    <section class="cover cover--charisma">
      <div class="cover-texture" role="img" aria-label="Faint tonal title pattern behind the word"></div>
      <h2 class="title">Charisma</h2>
    </section>
  </div>

  <div class="book" style="left:62px; top:430px;">
    <div class="book-shadow"></div><div class="book-gap"></div>
    <section class="cover cover--relationships">
      <div class="cover-texture" role="img" aria-label="Faint tonal title pattern behind the word"></div>
      <h2 class="title">Relationships</h2>
    </section>
  </div>

  <div class="book" style="left:342px; top:430px;">
    <div class="book-shadow"></div><div class="book-gap"></div>
    <section class="cover cover--results">
      <div class="cover-texture" role="img" aria-label="Faint tonal title pattern behind the word"></div>
      <h2 class="title">Results</h2>
    </section>
  </div>

  <div class="book" style="left:623px; top:430px;">
    <div class="book-shadow"></div><div class="book-gap"></div>
    <section class="cover cover--clarity">
      <div class="cover-texture" role="img" aria-label="Faint tonal title pattern behind the word"></div>
      <h2 class="title">Clarity</h2>
    </section>
  </div>

  <div class="book" style="left:904px; top:430px;">
    <div class="book-shadow"></div><div class="book-gap"></div>
    <section class="cover cover--being-present">
      <div class="cover-texture" role="img" aria-label="Faint tonal title pattern behind the word"></div>
      <h2 class="title">Being Present</h2>
    </section>
  </div>

  <div class="book" style="left:342px; top:809px;">
    <div class="book-shadow"></div><div class="book-gap"></div>
    <section class="cover cover--grooming">
      <div class="cover-texture" role="img" aria-label="Faint tonal title pattern behind the words"></div>
      <h2 class="title-phrase">
        <span class="big">Grooming</span>
        <span class="small">and</span>
        <span class="big">Appearance</span>
      </h2>
    </section>
  </div>

  <div class="book" style="left:623px; top:809px;">
    <div class="book-shadow"></div><div class="book-gap"></div>
    <section class="cover cover--acumen">
      <div class="cover-texture" role="img" aria-label="Faint tonal title pattern behind the word"></div>
      <h2 class="title">Acumen</h2>
    </section>
  </div>

</main>
</body>
</html>
```